Release Therapy business card that deals with the release of negative issues

I need a business card for my business called PEBBLES (A warm hearth to rest when you tire) ... I'm a therapist that deals with people releasing negative issues, by applying therapies that incorporate, hypnosis, aromatherapy and listen therapy..I like the colour green and soft blues...My idea is for a hand releasing butterflies, and incorporating soft clouds....
Target Market(s)
All people, all ages
Industry/Entity Type
Business
Contact Information for Business Card
PEBBLES"A Warm Hearth To Rest When You Tire"Yvette R BrockingtonRelease Therapist0411 743 781email: calmingpaths4you@quietmail.example
Requirements
Must have
- butterflies and soft clouds
Nice to have
- I like the decorative and script fonts for business name, and also my name
- Marisol T Fenwhistle...

```html
<!DOCTYPE html>
<html lang="en">
<head>
<meta charset="utf-8">
<title>PEBBLES – Business Card</title>
<link rel="stylesheet" href="https://fonts.googleapis.com/css2?family=Questrial&family=Pinyon+Script&display=swap">
<style>
  :root {
    --stage: #4a3540;
    --sky-top: #8fc6ea;
    --sky-mid: #cfe8f6;
    --cloud: #f4f9fd;
    --brand-blue: #2f63b8;
    --tagline-brown: #8a5a3c;
    --ink-blue: #1f3f9a;
    --skin: #e7b496;
    --butterfly-blue: #3fa9d6;
    --butterfly-gold: #e7b931;
  }
  * { box-sizing: border-box; margin: 0; padding: 0; }
  html, body { width: 1200px; height: 800px; overflow: hidden; }
  body {
    background: var(--stage);
    display: flex;
    align-items: center;
    justify-content: center;
    gap: 48px;
    font-family: "Questrial", sans-serif;
  }
  .card {
    position: relative;
    width: 530px;
    height: 303px;
    border-radius: 4px;
    overflow: hidden;
    box-shadow: 0 14px 30px rgba(0,0,0,.35);
  }
  .sky {
    position: absolute; inset: 0;
    background:
      radial-gradient(ellipse 60% 40% at 30% 65%, var(--cloud), transparent 70%),
      radial-gradient(ellipse 55% 35% at 75% 80%, var(--cloud), transparent 70%),
      radial-gradient(ellipse 45% 30% at 60% 35%, rgba(255,255,255,.8), transparent 70%),
      linear-gradient(170deg, var(--sky-top) 0%, var(--sky-mid) 55%, var(--cloud) 100%);
  }
  .brand-name {
    position: absolute;
    font-family: "Questrial", sans-serif;
    color: var(--brand-blue);
    letter-spacing: 2px;
    line-height: 1;
  }
  .tagline {
    position: absolute;
    font-family: "Pinyon Script", cursive;
    color: var(--tagline-brown);
    white-space: nowrap;
  }

  /* front */
  .front .butterflies-art {
    position: absolute; left: 40px; top: 24px; width: 150px; height: 52px;
    border-radius: 26px;
    background: linear-gradient(90deg, #3b7fd4, #c85bc0 50%, #49c0a8);
    opacity: .85;
  }
  .front .brand-name { left: 0; right: 0; top: 110px; text-align: center; font-size: 84px; }
  .front .tagline { left: 0; right: 0; top: 200px; text-align: center; font-size: 26px; }

  /* back */
  .back .hands-art {
    position: absolute; left: 24px; top: 30px; width: 230px; height: 240px;
    border-radius: 40% 50% 45% 40%;
    background:
      radial-gradient(circle at 65% 35%, var(--butterfly-blue) 0 22%, transparent 45%),
      radial-gradient(circle at 75% 20%, var(--butterfly-gold) 0 10%, transparent 30%),
      linear-gradient(200deg, rgba(255,255,255,0) 30%, var(--skin) 75%);
    opacity: .8;
  }
  .back .brand-name { right: 22px; top: 38px; font-size: 62px; }
  .back .tagline { right: 22px; top: 106px; font-size: 19px; }
  .contact {
    position: absolute; right: 22px; bottom: 24px;
    text-align: right;
    color: var(--ink-blue);
    line-height: 1.3;
  }
  .contact .person { font-size: 22px; }
  .contact .role { font-size: 14px; margin-bottom: 4px; }
  .contact .line { font-size: 15px; display: flex; align-items: center; justify-content: flex-end; gap: 6px; }
  .contact svg { width: 13px; height: 13px; fill: var(--ink-blue); }
</style>
</head>
<body>

  <section class="card front">
    <div class="sky" role="img" aria-label="Soft blue sky with white clouds"></div>
    <div class="butterflies-art" role="img" aria-label="Two rainbow-coloured butterflies"></div>
    <div class="brand-name">PEBBLES</div>
    <div class="tagline">A Warm Hearth To Rest When You Tire</div>
  </section>

  <section class="card back">
    <div class="sky" role="img" aria-label="Soft blue sky with white clouds"></div>
    <div class="hands-art" role="img" aria-label="Two open hands releasing blue and gold butterflies"></div>
    <div class="brand-name">PEBBLES</div>
    <div class="tagline">A Warm Hearth To Rest When You Tire</div>
    <div class="contact">
      <div class="person">Marisol T Fenwhistle</div>
      <div class="role">Release Therapist</div>
      <div class="line">
        <svg viewBox="0 0 24 24" aria-hidden="true"><path d="M6.6 10.8a15 15 0 0 0 6.6 6.6l2.2-2.2c.3-.3.7-.4 1-.2 1.1.4 2.3.6 3.6.6.6 0 1 .4 1 1V20c0 .6-.4 1-1 1A17 17 0 0 1 3 4c0-.6.4-1 1-1h3.5c.6 0 1 .4 1 1 0 1.3.2 2.5.6 3.6.1.3 0 .7-.2 1z"/></svg>
        0482 516 904
      </div>
      <div class="line">calmingpaths4you@quietmail.example</div>
    </div>
  </section>

</body>
</html>
```